Business card for Mortgage broker business

I have already had the logo designed and am needing a great looking business card. My business focus is on servicing clients who may not be able to obtain finance through traditional lenders due to bad credit, short term employment or they just don't fit the banks profile. It needs to be professional, trust worthy but also have a caring fell about it.
I have provided files showing the green and black logo, the white logo(on white background so the file looks blank) and also a file with the white logo with a background of leaves that was made up which will probably be used for a website header.

Industry/Entity Type

Finance

Contact Information for Business Card

Marcus Dalby
Managing Director, Accredited Finance Broker(AFB)
Po Box 817, Pakenham VIC 3810
marcus@kestrelfunding.com.au
www.kestrelfunding.com.au
0438 216 507

Requirements
Nice to have
• I have added a picture of myself as I would like to see some designs with the pic in it, but I'm not sure if I want it on there with the logo's or just the logo's

```html
<!DOCTYPE html>
<html lang="en">
<head>
<meta charset="utf-8">
<title>Kestrel Funding – Business Card</title>
<link href="https://fonts.googleapis.com/css2?family=Poppins:wght@400;500;600&display=swap" rel="stylesheet">
<style>
  :root {
    --brand-green: #1f7a45;
    --brand-green-dark: #17643a;
    --ink: #4a4a4a;
    --muted: #6f6f6f;
    --paper: #ffffff;
    --backdrop: #e9e7e2;
    --rule: #2a8450;
  }
  * { box-sizing: border-box; margin: 0; padding: 0; }
  html, body {
    width: 1200px; height: 843px; overflow: hidden;
    background: var(--backdrop);
    font-family: "Poppins", sans-serif;
  }
  .canvas {
    width: 1200px; height: 843px;
    display: flex; align-items: center; justify-content: center; gap: 40px;
  }
  .card {
    width: 520px; height: 300px;
    border-radius: 4px;
    box-shadow: 0 6px 18px rgba(0,0,0,.15);
    position: relative; overflow: hidden;
  }

  /* Front: green */
  .card--front {
    background: linear-gradient(135deg, var(--brand-green) 0%, var(--brand-green-dark) 100%);
    color: var(--paper);
    display: flex; flex-direction: column; align-items: center; justify-content: center;
  }
  .brand-name {
    display: flex; align-items: center; gap: 12px;
    font-weight: 600; letter-spacing: .5px; white-space: nowrap;
  }
  .brand-name__dot {
    width: 16px; height: 16px; border-radius: 50%;
    background: currentColor; flex: none;
  }
  .card--front .brand-name { font-size: 40px; color: var(--paper); }
  .front-web {
    margin-top: 26px;
    font-size: 13px; letter-spacing: 4px; color: var(--paper);
  }

  /* Back: white */
  .card--back { background: var(--paper); }
  .card--back .brand-name {
    position: absolute; top: 52px; right: 36px;
    font-size: 26px; color: var(--brand-green);
  }
  .contact {
    position: absolute; left: 34px; top: 112px; right: 34px;
    color: var(--ink);
  }
  .contact__name {
    font-size: 17px; font-weight: 600; color: var(--brand-green);
  }
  .contact__role {
    font-size: 12px; color: var(--muted); margin-bottom: 16px; white-space: nowrap;
  }
  .contact__line {
    font-size: 11.5px; line-height: 1.75; white-space: nowrap;
  }
  .contact__label {
    font-weight: 600; color: var(--brand-green);
  }
  .contact__item + .contact__item { margin-left: 14px; }
  .card__rule {
    position: absolute; left: 34px; right: 34px; bottom: 36px;
    height: 1.5px; background: var(--rule);
  }
</style>
</head>
<body>
  <main class="canvas">
    <section class="card card--front" aria-label="Business card front">
      <div class="brand-name"><span class="brand-name__dot"></span>Kestrel Funding</div>
      <div class="front-web">www.kestrelfunding.com.au</div>
    </section>

    <section class="card card--back" aria-label="Business card back">
      <div class="brand-name"><span class="brand-name__dot"></span>Kestrel Funding</div>
      <div class="contact">
        <p class="contact__name">Marcus Dalby</p>
        <p class="contact__role">Managing Director, Accredited Finance Broker (AFB)</p>
        <p class="contact__line">Po Box 817, Pakenham VIC 3810</p>
        <p class="contact__line">
          <span class="contact__item"><span class="contact__label">P</span> : 0438 216 507</span>
        </p>
        <p class="contact__line">
          <span class="contact__item"><span class="contact__label">E</span> : marcus@kestrelfunding.com.au</span>
          <span class="contact__item"><span class="contact__label">W</span> : www.kestrelfunding.com.au</span>
        </p>
      </div>
      <div class="card__rule"></div>
    </section>
  </main>
</body>
</html>
```